Steelcrest Process Systems. Needs a Business Card Design

We need a business card design for an engineering company which supplies industrial components (pumps, compressors, mechanical seals) provides repairs and services for above mentioned equipments. We offer a uniqe engineering solutions which help our customers to increase the productivness of their manufacturings, and energy savings.

Target Market(s)

Chemical and energy plants, refineries. Food industry and private consumers in a less.

Industry/Entity Type

Business

Contact Information for Business Card

Stylish and sleek design oriented on industrial area.

Requirements
Should not have
• company name shortening

```html
<!DOCTYPE html>
<html lang="en">
<head>
<meta charset="utf-8">
<title>Steelcrest Process Systems – Business Card</title>
<link href="https://fonts.googleapis.com/css2?family=Baloo+2:wght@600&family=Questrial&display=swap" rel="stylesheet">
<style>
  :root {
    --bg: #5a3a3a;
    --card-front: #ffffff;
    --card-back: #231f20;
    --brand-blue: #1226a3;
    --brand-red: #f2434b;
    --brand-orange: #fca044;
    --text-grey: #555555;
    --white: #ffffff;
  }
  html, body {
    margin: 0;
    padding: 0;
    width: 1200px;
    height: 1200px;
    overflow: hidden;
    background: var(--bg);
  }
  .canvas {
    position: relative;
    width: 1200px;
    height: 1200px;
  }
  .card {
    position: absolute;
    left: 186px;
    width: 832px;
    height: 472px;
    box-sizing: border-box;
    overflow: hidden;
  }
  .card--front { top: 98px; background: var(--card-front); }
  .card--back { top: 630px; background: var(--card-back); }

  .front-artwork {
    position: absolute;
    left: 420px;
    top: 52px;
    width: 412px;
    height: 420px;
    background: radial-gradient(ellipse 100% 100% at 85% 82%,
      var(--brand-blue) 0%,
      var(--brand-red) 30%,
      var(--brand-orange) 60%,
      rgba(252, 160, 68, 0) 100%);
  }

  .company-name {
    position: relative;
    font-family: "Baloo 2", sans-serif;
    font-weight: 600;
    margin: 0;
    line-height: 1;
    letter-spacing: 0.2px;
  }
  .card--front .company-name {
    position: absolute;
    left: 44px;
    top: 54px;
    font-size: 44px;
    color: var(--brand-blue);
    z-index: 1;
  }
  .person {
    position: absolute;
    left: 44px;
    top: 242px;
  }
  .person__name {
    font-family: "Baloo 2", sans-serif;
    font-weight: 600;
    font-size: 33px;
    line-height: 1;
    color: var(--brand-red);
    margin: 0;
  }
  .person__role {
    font-family: "Questrial", sans-serif;
    font-size: 23px;
    line-height: 1;
    color: var(--text-grey);
    margin: 6px 0 0;
  }
  .contacts {
    position: absolute;
    left: 44px;
    top: 334px;
    list-style: none;
    margin: 0;
    padding: 0;
    font-family: "Questrial", sans-serif;
    font-size: 23px;
    color: var(--text-grey);
  }
  .contacts li {
    display: flex;
    align-items: center;
    height: 28px;
    letter-spacing: 0.5px;
  }
  .contacts svg {
    width: 21px;
    height: 21px;
    margin-right: 11px;
    fill: var(--brand-blue);
    flex: none;
  }

  .back-mark {
    position: absolute;
    left: 348px;
    top: 134px;
    width: 136px;
    height: 136px;
    border-radius: 50%;
    background: var(--brand-red);
  }
  .card--back .company-name {
    position: absolute;
    left: 0;
    right: 0;
    top: 290px;
    text-align: center;
    font-size: 46px;
    color: var(--white);
  }
</style>
</head>
<body>
<main class="canvas">
  <section class="card card--front" aria-label="Card front">
    <div class="front-artwork" role="img" aria-label="Large decorative brand graphic in red, orange and blue"></div>
    <h1 class="company-name">Steelcrest Process Systems</h1>
    <div class="person">
      <p class="person__name">Daniel Reyes</p>
      <p class="person__role">Managing Partner</p>
    </div>
    <ul class="contacts">
      <li>
        <svg viewBox="0 0 20 20" aria-hidden="true"><path d="M1 7c0-3 4-5 9-5s9 2 9 5v1h-4V6H5v2H1zM4 9h12l2 9H2zm6 2.5a2.5 2.5 0 1 0 0 5 2.5 2.5 0 0 0 0-5z"/></svg>
        000.000.0000
      </li>
      <li>
        <svg viewBox="0 0 20 20" aria-hidden="true"><path d="M1 4h18v12H1zm2 2v8h14V6l-7 5zm1-0.5 6 4 6-4z" fill-rule="evenodd"/></svg>
        info@steelcrest.com
      </li>
      <li>
        <svg viewBox="0 0 20 20" aria-hidden="true"><path d="M10 1a9 9 0 1 0 0 18 9 9 0 0 0 0-18zm-1 2.1V6H6.6A7 7 0 0 1 9 3.1zm2 0A7 7 0 0 1 13.4 6H11zM5.6 8H9v3H3.1a7 7 0 0 1 2.5-3zm5.4 0h3.4a7 7 0 0 1 2.5 3H11zM3.3 13H9v3.9A7 7 0 0 1 3.3 13zm7.7 0h5.7A7 7 0 0 1 11 16.9z"/></svg>
        www.steelcrest.com
      </li>
    </ul>
  </section>

  <section class="card card--back" aria-label="Card back">
    <div class="back-mark" aria-hidden="true"></div>
    <p class="company-name">Steelcrest Process Systems</p>
  </section>
</main>
</body>
</html>
```